Business card design for a engineering company

I need a double sided business card design for my company "Verdmont Flow Solutions". The card will be used in Malaysia. Sleek and professional, with a little design flare to it.
Information to showcase:
1. Company logo
2. Name, title, phone, email address, website address
3. our products "Pumping technology, Valve & actuation, Air Moving Technology
Example:
Ravi Tanaka
Business manager
ravi.tanaka@verdmont-example.com
www.verdmont-example.com.my
- Pumping technology
- Valve & actuation
- Air moving technology
Target Market(s)
engineers, purchasing managers
Industry/Entity Type
Business
Contact Information for Business Card
Ravi Tanaka
Business manager
ravi.tanaka@verdmont-example.com
www.verdmont-example.com.my
- Pumping technology
- Valve & actuation
- Air moving technology
catch phrase : "Solving flow challenges, exceeding expectations"

```html
<!DOCTYPE html>
<html lang="en">
<head>
<meta charset="utf-8">
<title>Verdmont Flow Solutions – Business Card</title>
<link rel="stylesheet" href="https://fonts.googleapis.com/css2?family=Source+Sans+3:wght@400;600;700&display=swap">
<style>
  :root {
    --navy: #0b3142;
    --orange: #f39a1d;
    --orange-deep: #ef6f25;
    --yellow: #ffc61a;
    --ink: #3d4448;
    --paper: #ffffff;
    --backdrop: #e9e7e3;
  }
  * { box-sizing: border-box; margin: 0; padding: 0; }
  html, body {
    width: 1200px; height: 987px; overflow: hidden;
    background: var(--backdrop);
    font-family: "Source Sans 3", sans-serif;
  }
  .canvas { position: relative; width: 1200px; height: 987px; }
  .card {
    position: absolute; left: 293px; width: 615px; height: 352px;
    box-shadow: 0 2px 6px rgba(0,0,0,0.18);
    overflow: hidden;
  }
  .card--front { top: 130px; background: var(--paper); }
  .card--back { top: 505px; background: var(--navy); }

  .brand { position: absolute; left: 38px; top: 52px; display: flex; align-items: center; gap: 16px; }
  .brand__dot { width: 54px; height: 54px; border-radius: 50%; background: var(--navy); }
  .brand__name { font-size: 30px; font-weight: 600; color: var(--navy); letter-spacing: 0.5px; }

  .band {
    position: absolute; left: 0; top: 159px; width: 615px; height: 66px;
    background: var(--navy);
  }
  .band__glow {
    position: absolute; right: 0; top: 0; width: 135px; height: 66px;
    background: radial-gradient(circle at 70% 50%, var(--yellow) 0%, var(--orange) 35%, var(--orange-deep) 100%);
  }
  .band__name {
    position: absolute; left: 38px; top: 8px;
    font-size: 23px; font-weight: 700; color: var(--orange); letter-spacing: 0.3px;
  }
  .band__title {
    position: absolute; left: 36px; top: 36px;
    font-size: 17px; font-weight: 400; color: var(--paper);
  }

  .contact { position: absolute; left: 38px; top: 252px; list-style: none; }
  .contact li {
    display: flex; align-items: center; gap: 8px;
    height: 23.5px; font-size: 16.5px; color: var(--ink);
  }
  .contact svg { width: 14px; height: 14px; fill: var(--navy); flex: none; }

  .products { position: absolute; right: 34px; top: 255px; list-style: none; text-align: right; }
  .products li {
    height: 22px; font-size: 16.5px; color: var(--ink);
    display: flex; justify-content: flex-end; align-items: center; gap: 10px;
  }
  .products li::after {
    content: ""; width: 6px; height: 6px; border-radius: 50%; background: var(--navy);
  }

  .back-brand {
    position: absolute; left: 0; top: 92px; width: 615px;
    display: flex; flex-direction: column; align-items: center; gap: 20px;
  }
  .back-brand__dot { width: 92px; height: 92px; border-radius: 50%; background: var(--orange); }
  .back-brand__name { font-size: 30px; font-weight: 600; color: var(--paper); letter-spacing: 0.5px; }
  .tagline {
    position: absolute; left: 0; top: 294px; width: 615px; text-align: center;
    font-size: 16.5px; color: var(--paper);
  }
</style>
</head>
<body>
<main class="canvas">
  <section class="card card--front" aria-label="Card front">
    <div class="brand">
      <span class="brand__dot"></span>
      <span class="brand__name">Verdmont Flow Solutions</span>
    </div>

    <div class="band">
      <div class="band__glow"></div>
      <p class="band__name">RAVI TANAKA</p>
      <p class="band__title">Business manager</p>
    </div>

    <ul class="contact">
      <li>
        <svg viewBox="0 0 16 16" aria-hidden="true"><path d="M3.6 1.2l2.3 2.6-1.3 1.9c.9 2 2.6 3.8 4.7 4.8l1.9-1.3 2.6 2.3-1.3 2.4C7.9 14.3 1.7 8.1 1.2 2.5z"/></svg>
        600 555 0142
      </li>
      <li>
        <svg viewBox="0 0 16 16" aria-hidden="true"><path d="M1 3h14v1.2L8 9 1 4.2z"/><path d="M1 5.6l7 4.8 7-4.8V13H1z"/></svg>
        ravi.tanaka@verdmont-example.com
      </li>
      <li>
        <svg viewBox="0 0 16 16" aria-hidden="true"><circle cx="8" cy="8" r="7"/><path d="M4 5c1.5 0 2.5 1 2 2.5S4 9 5 11l1 2.4C3 12.6 1.5 10 1.8 7.2 2.3 6 3 5 4 5zM10 2.3c1 1 .4 2.2-.6 2.6s-1 1.6.3 2 2.4 1.4 1.6 3.3l-.8 1.6c2-1 3.3-3.2 3.3-5.5-.5-2-2-3.5-3.8-4z" fill="#fff"/></svg>
        www.verdmont-example.com.my
      </li>
    </ul>

    <ul class="products">
      <li>Pumping technology</li>
      <li>Valve &amp; actuation</li>
      <li>Air moving technology</li>
    </ul>
  </section>

  <section class="card card--back" aria-label="Card back">
    <div class="back-brand">
      <span class="back-brand__dot"></span>
      <span class="back-brand__name">Verdmont Flow Solutions</span>
    </div>
    <p class="tagline">Solving flow challenges, exceeding expectations</p>
  </section>
</main>
</body>
</html>
```